website for cartnest- Almond Valet. Natural Peanut Butter Mixer

I need a website for cartnest for my invention...The AlmondValet. ( Registered trademark)
They are kitchen accessories for mixing Natural peanut butter (9 mixing hooks). Natural peanut butter separates with oil floating to the top when it sits on the shelf. Very hard and messy to mix it in manually.

My hook is compatible with 8 popular brand name electric hand mixers, plus 1/4” HEX universal drill bit. (9 total)

The mixing Hook part that goes into the nut butter is all the same for each hook, it’s just locking interface changes for each hook. I will supply a close up photo for each hook lock mechanism. ( leave blank until Thursday next week)
Brands are: Grey and Mallory, Vexomart, Corwin Harbor, StoveMate, Pryle, Dunmore Vaxil, Glowfield Modern, Glowfield Retro.
Plus 1/4” HEX quick lock drill bit.

I would like to inspire with complementary healthy peanut butter snack images..as peanut butter is pretty brown!!
There are lots of beautiful stock photos of peanut butter snacks on lensvault or Pixbarn. Samples included in my files. My logo needs to have Registered trade Mark R in circle ⭕️ added to end of logo.
Plus I would like a couple of smiling moms with kids eating peanut butter.

Target Market(s)

North American health food minded people.

Coding

Coded - Design and coding required

Number of Pages Required

5+ page

Font styles to use
Sans Serif

Colors
ffffff
ec1f27
f78f20
9bcb3c

Requirements
Must have
• I have about 6 sections in my 1 page website to design....page 7 thru 15 are all the same with just photo and brand name changes and list of model numbers compatible, for each different mixing hook.

I want my headline to rotate with 3 changing words.
Natural Peanut Butter
1) Mixed Perfectly 2) Better Tasting 3) Hassle-Free

Want to add shop now button on all pages.

Clean white background. I like shadow colour boxes behind clusters of 2-3 photos. Contemporary look.
I can type and upload blog pages soon so you don’t have to type them in. Just add a few photos.
Patented Design!!! Important to add so copy cats don’t copy.
Nice to have
• Complementary 3 colour palette that doesn’t change. Red being one.
Open to seeing other colour palettes.
Should not have
• Logos of any brand names. Just written in a clear black font consistent for all.

```html
<!DOCTYPE html>
<html lang="en">
<head>
<meta charset="utf-8">
<title>Almond Valet – The Natural Peanut Butter Mixer</title>
<link href="https://fonts.googleapis.com/css2?family=Michroma&family=Poppins:wght@400;500;600&display=swap" rel="stylesheet">
<style>
:root{
  --white:#ffffff;
  --ink:#1d1a19;
  --grey:#8a8a8a;
  --light:#efefef;
  --orange:#c7811c;
  --salmon:#d5937b;
  --rose:#8f5c4f;
  --button:#7a4a3e;
  --dark:#2f2523;
  --star:#e3a526;
  --photo-warm:#c9925d;
}
*{box-sizing:border-box;margin:0;padding:0}
html,body{width:1200px;height:5181px;overflow:hidden;background:var(--white)}
body{font-family:"Poppins",sans-serif;color:var(--ink)}
.page{position:relative;width:1200px;height:5181px;overflow:hidden}
.abs{position:absolute}
.backdrop{position:absolute;left:0;top:0}
.heading{font-family:"Michroma",sans-serif;text-transform:uppercase;letter-spacing:1px}
.photo{position:absolute;background:radial-gradient(circle at 40% 40%,#e3b98a,var(--photo-warm) 60%,#9a6a43)}
.photo.round{border-radius:50%}
.btn{position:absolute;background:var(--button);color:var(--white);font-weight:600;font-size:14px;letter-spacing:.5px;border-radius:24px;display:flex;align-items:center;justify-content:center;box-shadow:0 6px 14px rgba(0,0,0,.18)}

/* header */
.brand-small{left:90px;top:40px;font-family:"Michroma",sans-serif;font-size:17px;color:var(--rose);letter-spacing:1px}
.brand-small .dot{display:inline-block;width:26px;height:26px;border-radius:50%;background:var(--rose);vertical-align:middle;margin-right:8px}
.nav{right:88px;top:45px;display:flex;gap:32px;font-size:13px;font-weight:600}
.brand-main{left:0;width:1200px;top:196px;text-align:center;font-family:"Michroma",sans-serif;font-size:46px;color:var(--ink);letter-spacing:2px}
.brand-main sup{font-size:18px;font-family:"Poppins",sans-serif;vertical-align:top;position:relative;top:4px}
.tagline{left:0;width:1200px;top:258px;text-align:center;font-family:"Michroma",sans-serif;font-size:14px;letter-spacing:6px;color:var(--ink)}

/* how it works */
.how-title{left:0;width:1200px;top:952px;text-align:center;color:var(--white);font-size:34px}
.step{position:absolute;display:flex;align-items:center;gap:20px;color:var(--white);font-size:14px;line-height:22px;width:300px}
.step .ico{width:88px;height:88px;border-radius:50%;background:rgba(255,255,255,.2);display:flex;align-items:center;justify-content:center;flex:none}
.shop-link{left:0;width:1200px;top:1398px;text-align:center;color:var(--white);font-weight:600;font-size:17px;text-decoration:underline;text-underline-offset:5px}

/* price */
.price{left:0;width:1200px;top:1510px;text-align:center;color:var(--white);font-size:96px;font-weight:600;letter-spacing:1px}
.price sup{font-size:26px;vertical-align:top;position:relative;top:22px;margin-left:12px}
.price-note{left:0;width:1200px;top:1628px;text-align:center;color:var(--white);font-size:15px}
.form{position:absolute;width:508px;height:56px;background:var(--white);border-radius:30px;display:flex;align-items:center;padding:0 5px 0 26px;box-shadow:0 4px 14px rgba(0,0,0,.1)}
.form.outlined{border:4px solid var(--white);box-shadow:0 0 0 2px rgba(255,255,255,.35)}
.form .field{flex:1;font-size:13px;color:#9a9a9a;display:flex;align-items:center;gap:10px}
.form .submit{width:156px;height:44px;border-radius:24px;background:var(--button);color:var(--white);font-weight:600;font-size:14px;display:flex;align-items:center;justify-content:center;letter-spacing:.5px}

/* hooks */
.hooks-title{left:0;width:1200px;top:2036px;text-align:center;font-size:34px}
.brand-chip{position:absolute;border-radius:50%;background:var(--light);display:flex;align-items:center;justify-content:center;text-align:center;font-weight:600;color:var(--ink);line-height:1.15}

/* description */
.desc-title{left:705px;top:2652px;font-size:34px}
.desc-text{left:705px;top:2700px;font-size:15px;line-height:27px;color:#555;width:460px}

/* mixes */
.mix-title{left:0;width:1200px;top:3052px;text-align:center;font-size:34px;line-height:36px}
.mix-sub{left:0;width:1200px;top:3138px;text-align:center;font-size:20px;color:#b4b4b4}

/* testimonials */
.say-title{left:0;width:1200px;top:3660px;text-align:center;color:var(--white);font-size:34px;line-height:36px}
.card{position:absolute;top:3768px;width:420px;height:234px;background:var(--white);border-radius:0 70px 70px 70px;padding:30px 40px 0 46px}
.card .who{display:flex;align-items:center;gap:14px}
.card .avatar{width:64px;height:64px;border-radius:50%;background:linear-gradient(135deg,#c8b6aa,#6d5a52)}
.card .name{color:var(--rose);font-weight:600;font-size:16px}
.card .stars{color:var(--star);font-size:19px;letter-spacing:2px;line-height:22px}
.card .quote{position:absolute;right:38px;top:22px;font-family:"Michroma",sans-serif;font-size:80px;color:#e6e6e6;line-height:1}
.card p{margin-top:18px;font-size:13px;line-height:22px;color:#555}
.arrows{left:560px;top:4060px;color:rgba(255,255,255,.6);font-size:22px;letter-spacing:20px}

/* signup */
.sign-title{left:0;width:1200px;top:4378px;text-align:center;font-size:34px}
.sign-sub{left:0;width:1200px;top:4424px;text-align:center;font-size:15px;font-weight:500;color:#444}

/* footer */
.hungry{left:0;width:1200px;top:4752px;text-align:center;color:var(--white);font-size:34px}
.foot-brand{left:86px;top:4962px;color:var(--white);font-family:"Michroma",sans-serif;font-size:14px;letter-spacing:.5px;white-space:nowrap}
.foot-brand .dot{display:inline-block;width:28px;height:28px;border-radius:50%;background:var(--white);vertical-align:middle;margin-right:10px}
.foot-col{position:absolute;top:4908px;color:var(--white);font-size:13px;line-height:31px}
.foot-col h4{font-size:13px;font-weight:600;letter-spacing:.5px;line-height:20px;margin-bottom:8px}
.social{display:flex;gap:12px;margin-top:10px}
.social span{width:32px;height:32px;border-radius:50%;background:rgba(255,255,255,.15)}
.foot-form{position:absolute;left:836px;top:4944px;width:276px;height:40px;background:var(--white);border-radius:20px;display:flex;align-items:center;padding-left:22px;font-size:13px;color:#555}
.foot-form .go{position:absolute;right:0;top:0;width:58px;height:40px;border-radius:20px;background:var(--salmon);display:flex;align-items:center;justify-content:center}
.foot-rule{left:0;top:5100px;width:1200px;height:1px;background:rgba(255,255,255,.2)}
.copyright{left:0;width:1200px;top:5138px;text-align:center;color:var(--white);font-size:12px;font-weight:500;letter-spacing:.5px}
.to-top{left:1128px;top:5094px;width:46px;height:46px;border-radius:50%;background:var(--white);display:flex;align-items:center;justify-content:center}
</style>
</head>
<body>
<div class="page">

  <svg class="backdrop" width="1200" height="5181" viewBox="0 0 1200 5181" aria-hidden="true">
    <path fill="var(--salmon)" d="M0 1330 L1200 1300 L1200 1790 C1030 1900 830 1990 600 1990 C360 1990 160 1900 0 1820 Z"/>
    <path fill="var(--orange)" d="M0 880 C180 660 480 560 760 520 C950 495 1100 560 1200 640 L1200 1330 C1000 1350 760 1370 600 1380 C380 1390 160 1380 0 1390 Z"/>
    <circle cx="598" cy="1418" r="92" fill="var(--salmon)"/>
    <path fill="var(--salmon)" d="M40 2560 C120 2480 300 2490 420 2520 C560 2560 630 2660 600 2760 C570 2880 460 2940 380 3000 C300 3060 160 3090 90 3020 C20 2960 0 2860 0 2760 L0 2620 Z"/>
    <path fill="var(--rose)" d="M0 3460 C120 3440 320 3470 520 3480 C720 3495 840 3560 1000 3590 C1100 3605 1160 3600 1200 3590 L1200 4010 C1000 4030 800 4100 600 4170 C400 4230 200 4230 0 4220 Z"/>
    <path fill="var(--dark)" d="M0 4880 C160 4740 420 4650 700 4660 C920 4668 1080 4700 1200 4650 L1200 5181 L0 5181 Z"/>
  </svg>

  <!-- header -->
  <div class="abs brand-small"><span class="dot"></span>ALMOND VALET</div>
  <nav class="abs nav"><span>BLOG</span><span>HELP</span></nav>
  <div class="abs brand-main">ALMOND VALET<sup>®</sup></div>
  <div class="abs tagline">THE NATURAL PEANUT BUTTER MIXER</div>
  <div class="btn" style="left:523px;top:293px;width:154px;height:46px">SHOP NOW</div>

  <!-- hero photos -->
  <div class="photo" role="img" aria-label="Jar of natural peanut butter with a spiral mixing hook, surrounded by peanuts" style="left:360px;top:345px;width:580px;height:520px;border-radius:48% 48% 40% 40%;background:radial-gradient(ellipse at 50% 45%,#b88050,#9a6638 45%,rgba(199,129,28,0) 72%)"></div>
  <div class="photo" role="img" aria-label="Peanuts spilling from the left edge" style="left:-40px;top:720px;width:150px;height:170px;border-radius:50%"></div>
  <div class="photo round" role="img" aria-label="Bowl of creamy peanut butter with a mixing hook" style="left:-60px;top:1050px;width:330px;height:330px"></div>
  <div class="photo round" role="img" aria-label="Bowl of peanut butter swirl with nuts" style="left:1060px;top:820px;width:360px;height:360px;background:radial-gradient(circle,#f1ddc4,#d9ad7b)"></div>

  <!-- how it works -->
  <h2 class="abs heading how-title">HOW IT WORKS</h2>
  <div class="step" style="left:314px;top:1034px">
    <span class="ico"><svg width="42" height="42" viewBox="0 0 42 42" fill="none" stroke="#fff" stroke-width="2.5" stroke-linecap="round"><rect x="6" y="6" width="30" height="12" rx="4"/><path d="M21 18v8M16 26h10l-2 10h-6z"/></svg></span>
    <span>Use your own hand<br>mixer or drill</span>
  </div>
  <div class="step" style="left:608px;top:1034px">
    <span class="ico"><svg width="42" height="42" viewBox="0 0 42 42" fill="none" stroke="#fff" stroke-width="2.5" stroke-linecap="round"><path d="M24 4v22a7 7 0 0 1-14 0v-4"/><path d="M20 4h8"/></svg></span>
    <span>Thin-2 mm Stainless<br>Steel hook mixes<br>without displacing oil</span>
  </div>
  <div class="step" style="left:314px;top:1160px">
    <span class="ico"><svg width="42" height="42" viewBox="0 0 42 42" fill="none" stroke="#fff" stroke-width="2.5" stroke-linejoin="round"><rect x="11" y="4" width="20" height="6" rx="1"/><rect x="9" y="10" width="24" height="28" rx="3"/><rect x="14" y="18" width="14" height="12"/></svg></span>
    <span>Mix it right in your<br>store-bought jar.</span>
  </div>
  <div class="step" style="left:608px;top:1160px">
    <span class="ico"><svg width="42" height="42" viewBox="0 0 42 42" fill="#fff"><path d="M6 26c8-2 14-10 26-16-4 10-12 20-26 16z"/><path d="M8 32c10 2 20-2 28-8-4 8-14 14-28 8z"/></svg></span>
    <span>Arrow Tip breaks up<br>settled nuts creating<br>top to bottom flow.</span>
  </div>
  <div class="abs shop-link">SHOP NOW</div>

  <!-- price -->
  <div class="photo round" role="img" aria-label="Hand mixer blending peanut butter in a jar beside peanuts" style="left:-40px;top:1500px;width:300px;height:340px"></div>
  <div class="photo" role="img" aria-label="Hand holding a jar under an electric hand mixer" style="left:880px;top:1460px;width:320px;height:470px;border-radius:40% 0 0 50%;background:linear-gradient(160deg,#e9e9e6,#bdb7b0 50%,#8d6a4c)"></div>
  <div class="photo round" role="img" aria-label="Small bowl of whipped peanut butter" style="left:745px;top:1845px;width:148px;height:148px"></div>
  <div class="abs price">$19.99<sup>USD</sup></div>
  <div class="abs price-note">Sign up for Free shipping Coupon (Valid in USA and Canada only)</div>
  <div class="form outlined" style="left:346px;top:1688px">
    <span class="field"><svg width="16" height="12" viewBox="0 0 16 12"><rect width="16" height="12" rx="2" fill="#8a8a8a"/><path d="M1 1l7 6 7-6" stroke="#fff" stroke-width="1.4" fill="none"/></svg>Enter your email address</span>
    <span class="submit">SUBSCRIBE</span>
  </div>

  <!-- hooks -->
  <h2 class="abs heading hooks-title">CHOOSE YOUR HOOK HOW</h2>
  <div class="brand-chip" style="left:314px;top:2115px;width:140px;height:140px;font-size:24px">Pryle</div>
  <div class="brand-chip" style="left:748px;top:2121px;width:136px;height:136px;font-size:14px">Glowfield<br>Modern</div>
  <div class="brand-chip" style="left:543px;top:2179px;width:124px;height:124px;font-size:14px">Corwin<br>Harbor</div>
  <div class="brand-chip" style="left:404px;top:2284px;width:112px;height:112px;font-size:14px">Vexomart</div>
  <div class="brand-chip" style="left:217px;top:2326px;width:120px;height:120px;font-size:14px">Grey and<br>Mallory</div>
  <div class="brand-chip" style="left:664px;top:2304px;width:136px;height:136px;font-size:14px">Dunmore<br>Vaxil</div>
  <div class="brand-chip" style="left:863px;top:2324px;width:116px;height:116px;font-size:14px">StoveMate</div>
  <div class="brand-chip" style="left:150px;top:2160px;width:116px;height:116px;font-size:14px">Glowfield<br>Retro</div>
  <div class="brand-chip" style="left:940px;top:2170px;width:116px;height:116px;font-size:14px">1/4” HEX<br>Drill Bit</div>

  <!-- description -->
  <div class="photo" role="img" aria-label="Smiling mother and daughter eating bread with peanut butter in the kitchen" style="left:0;top:2505px;width:600px;height:480px;border-radius:30% 45% 50% 40% / 25% 60% 45% 55%;background:linear-gradient(135deg,#d9c5b3,#a88068 55%,#6f5448)"></div>
  <h2 class="abs heading desc-title">DESCRIPTION</h2>
  <p class="abs desc-text">Mother and daughter breakfast in the kitchen.<br>Cute little girl eats bread with peanut butter.<br>Looking at Camera</p>
  <div class="photo" role="img" aria-label="Scattered peanuts and almonds" style="left:1025px;top:2885px;width:200px;height:200px;border-radius:50%;background:radial-gradient(circle,#d8b48c,#a46b3e 60%,rgba(255,255,255,0) 72%)"></div>

  <!-- mixes -->
  <h2 class="abs heading mix-title">MIXES IN ALL NATURAL<br>NUT BUTTERS</h2>
  <div class="abs heading mix-sub">RIGHT IN THEIR OWN JARS.</div>
  <div class="photo" role="img" aria-label="Five colourful jars in blue, yellow, pink, green and purple on a wooden shelf" style="left:85px;top:3225px;width:1030px;height:320px;border-radius:16px;background:linear-gradient(90deg,#4cb3ec,#f2c21c 28%,#f27a7d 50%,#6fd25a 72%,#a66ae8)"></div>

  <!-- testimonials -->
  <h2 class="abs heading say-title">WHAT PEOPLE<br>ARE SAYING...</h2>
  <div class="card" style="left:90px">
    <span class="quote">“</span>
    <div class="who"><span class="avatar" role="img" aria-label="Customer portrait"></span><div><div class="name">Dorian Welk</div><div class="stars">★★★★<span style="color:#ddd">★</span></div></div></div>
    <p>"Integer tincidunt cras dapibus vivamus tum semper nisi aenean vulputate eleifend tellus aenean leo ligula, porttitor eu consequat vitae, eleifend ac, enim aliquam dapibus"...</p>
  </div>
  <div class="card" style="left:537px">
    <span class="quote">“</span>
    <div class="who"><span class="avatar" role="img" aria-label="Customer portrait"></span><div><div class="name">Milo Arden</div><div class="stars">★★★★<span style="color:#ddd">★</span></div></div></div>
    <p>"Integer tincidunt cras dapibus vivamus tum semper nisi aenean vulputate eleifend tellus aenean leo ligula, porttitor eu consequat vitae, eleifend ac, enim aliquam dapibus"...</p>
  </div>
  <div class="card" style="left:984px">
    <span class="quote">“</span>
    <div class="who"><span class="avatar" role="img" aria-label="Customer portrait"></span><div><div class="name">Milo Arden</div><div class="stars">★★★★<span style="color:#ddd">★</span></div></div></div>
    <p>"Integer tincidunt cras dapibus vivamus tum semper nisi aenean vulputate eleifend tellus aenean leo ligula, porttitor eu consequat vitae, eleifend ac, enim aliquam dapibus"...</p>
  </div>
  <div class="abs arrows">←→</div>

  <!-- signup -->
  <div class="photo round" role="img" aria-label="Bowl of whipped natural peanut butter" style="left:214px;top:4060px;width:256px;height:256px;border:10px solid #fff;box-shadow:0 10px 24px rgba(0,0,0,.15)"></div>
  <h2 class="abs heading sign-title">SIGN UP FOR FREE SHIPPING + GET</h2>
  <div class="abs sign-sub">12 Natural Peanut Butter Mixing Hacks!....That actually Work</div>
  <div class="form" style="left:346px;top:4484px;border:1px solid #eee">
    <span class="field"><svg width="16" height="12" viewBox="0 0 16 12"><rect width="16" height="12" rx="2" fill="#8a8a8a"/><path d="M1 1l7 6 7-6" stroke="#fff" stroke-width="1.4" fill="none"/></svg>Enter your email address</span>
    <span class="submit">SUBSCRIBE</span>
  </div>

  <!-- footer -->
  <h2 class="abs heading hungry">HUNGRY FOR MORE?</h2>
  <div class="btn" style="left:523px;top:4808px;width:154px;height:46px">SHOP NOW</div>
  <div class="abs foot-brand"><span class="dot"></span>ALMOND VALET</div>
  <div class="foot-col" style="left:336px"><div>Shops</div><div>Hooks</div><div>Blogs</div></div>
  <div class="foot-col" style="left:448px"><div>Help</div><div>Peanut Butter</div><div>Recipies</div><div>Return +</div><div>Warranty</div></div>
  <div class="foot-col" style="left:597px">
    <h4>CONTACT US</h4>
    <div style="line-height:20px">info@almondvaletmail.com</div>
    <div class="social"><span></span><span></span></div>
  </div>
  <div class="foot-col" style="left:836px"><h4>SIGNUP FOR FREE SHIPPING</h4></div>
  <div class="foot-form">Email address
    <span class="go"><svg width="18" height="18" viewBox="0 0 18 18"><path d="M1 8l16-7-6 16-2-7z" fill="#fff"/></svg></span>
  </div>
  <div class="abs foot-rule"></div>
  <div class="abs to-top"><svg width="18" height="18" viewBox="0 0 18 18" fill="none" stroke="#2f2523" stroke-width="2" stroke-linecap="round"><path d="M9 15V3M4 8l5-5 5 5"/></svg></div>
  <div class="abs copyright">© COPYRIGHT 2021 ALMOND VALET ALL RIGHTS RESERVED</div>

</div>
</body>
</html>
```